Need a clean & modern homepage for an education site + opportunity for longer term work

Thanks for viewing our project. We are excited about this new website and we hope that we might build a relationship with designers as we work on this project. I provided quite a few details and requirements to help you more quickly create a design that meets our needs.
Who we are:
We are a website that discusses the importance of college accreditation and provides a directory of college programs.
What we need:
A homepage that meets the below requirements and is inspired by the examples provided
Definition of accredited:
ac·cred·it·ed [uh-kred-i-tid] adj.
1. officially recognized as meeting the essential requirements, as of academic excellence: accredited schools.
2. provided with official credentials, as by a government: an accredited diplomatic representative.
3. accepted as authoritative: an accredited theory.
Overall look and feel for the homepage:
- Clean, simple and modern
- Limited (or zero) pictures
- Utilize color blocks with text
- A trend seems to be longer vertical length homepages with lots of whitespace. I generally like this trend as long as the page is not way to tall.
Inspirations: Sites that have a similar look and feel to what I need.
http://plinvar.org/
http://www.tumbrelstat.com/colleges/harrowgate-university/
http://quietmarble.org/
http://www.vellichorstaffing.com/
http://www.plonk.com/
http://sketches.zimvo.com/
Items to be included on the homepage. Details below on each item.
- Top navigation
- Logo: Please leave a blank area for a logo. The logo has not been designed.
- Simple graphic/color block at the top that highlights a definition of “Accredited” – the definition should be formatted like it is being copy/pasted from a dictionary.
- Space for a video and small (50 word) written description of the video. You can use placeholder text.
- One section with 3 Paragraphs of content (each paragraph around 100 words) with a header at the top. You can use placeholder text but please create the formatting. At the end of the 3 paragraphs please have a “Read More” Note this shouldn't be 3 separate paragraphs with three read mores - it is 3 paragraphs with one read more at the end.
- An area with the header “Search Colleges by State” that has anchor text links to all 50 states.
Top navigation:
- Home
- States – with a subnav dropdown that includes all 50 US states.
- Programs – with a subnav dropdown that includes program titles (list below)
- Degrees - with a subnav dropdown that includes 5 degree levels (list below)
- Accreditation – no subnav
- Rankings – no subnav
- Resources – no subnav
Footer
- Link to about us, privacy, and a copyright www.url.com
Programs List for sub navigation
Accounting
Art
Bible
Business
Criminal Justice
Design
Engineering
English
Law
LPN to RN
Management
Math
MBA
MPH
Medical Assisting
Military
Nursing
Occupational Therapy
Paralegal
Psychology
Pharmacy
RN to BSN
Radiology
Social Work
Sonography
Degrees list for sub navigation
Certificate
Associate
Bachelors
Masters
PhD
Thanks so much - looking forward to working with you!

```html
<!DOCTYPE html>
<html lang="en">
<head>
<meta charset="utf-8">
<title>Accredited – Homepage</title>
<link rel="stylesheet" href="https://fonts.googleapis.com/css2?family=Arimo:wght@400;700&display=swap">
<style>
  :root{
    --canvas:#ececec;
    --teal:#00a7c4;
    --white:#ffffff;
    --ink:#111111;
    --body:#444444;
    --footer:#454545;
    --footer-deep:#2b2b2b;
    --footer-text:#b4b4b4;
    --field:#7b7b7b;
    --button:#4a4a4a;
    --video-dark:#141414;
    --video-mid:#3a2e22;
  }
  *{box-sizing:border-box;margin:0;padding:0}
  html,body{width:1200px;height:1000px;overflow:hidden;background:var(--canvas);font-family:"Arimo",Arial,sans-serif}
  .page{position:absolute;left:100px;top:116px;width:1000px;background:var(--white)}

  .site-header{position:relative;height:131px;background:var(--teal)}
  .brand{position:absolute;left:150px;top:30px;font-size:56px;font-weight:400;color:var(--white);letter-spacing:1px}
  .main-nav{position:absolute;right:100px;top:102px;display:flex;gap:24px}
  .main-nav a{position:relative;color:var(--white);font-size:13.5px;font-weight:700;text-decoration:none}
  .main-nav a.has-sub::after{content:"";position:absolute;left:50%;top:20px;margin-left:-6px;border-left:6px solid transparent;border-right:6px solid transparent;border-top:7px solid var(--white)}

  .intro{position:relative;height:330px}
  .definition{position:absolute;left:109px;top:28px;font-size:22px;font-weight:700;color:var(--ink)}
  .video{position:absolute;left:95px;top:63px;width:358px;height:217px;background:var(--video-dark)}
  .video-still{position:absolute;inset:0 0 16px 0;background:radial-gradient(ellipse at 50% 55%,var(--video-mid),var(--video-dark) 75%)}
  .video-title{position:absolute;left:0;right:0;top:20px;text-align:center;color:var(--white);font-size:12px;font-weight:700}
  .video-play{position:absolute;left:160px;top:88px}
  .video-controls{position:absolute;left:0;right:0;bottom:0;height:16px;background:#1e1e1e;border-top:2px solid #7a1f1f}
  .video-controls svg{position:absolute;top:3px}
  .video-caption{position:absolute;left:95px;top:284px;width:358px;text-align:center;font-size:11px;line-height:15px;color:var(--body)}
  .overview{position:absolute;left:463px;top:69px;width:441px}
  .overview h2{font-size:23px;font-weight:700;color:var(--teal);margin-bottom:10px}
  .overview p{font-size:10.5px;line-height:12.5px;color:var(--body)}
  .overview p + p{margin-top:35px}
  .read-more{position:absolute;right:100px;top:302px;font-size:10.5px;color:var(--ink);text-decoration:none}

  .state-search{position:relative;height:58px;background:var(--teal)}
  .search-field{position:absolute;left:334px;top:13px;width:289px;height:32px;background:var(--field);color:var(--white);font-size:11px;line-height:32px;padding-left:18px}
  .search-button{position:absolute;left:623px;top:13px;width:42px;height:32px;background:var(--button)}
  .search-button svg{position:absolute;left:9px;top:4px}

  .site-footer{position:relative;height:200px;background:var(--footer)}
  .footer-col{position:absolute;top:14px;list-style:none}
  .footer-col li{font-size:10.5px;line-height:15px;color:var(--footer-text)}
  .col-about{left:95px}.col-programs-a{left:258px}.col-programs-b{left:399px}.col-programs-c{left:547px}
  .col-degrees{left:718px;width:182px}
  .col-degrees .footer-heading{color:var(--white);font-weight:700;border-bottom:1px solid var(--white);margin-bottom:2px}
  .copyright{height:48px;background:var(--footer-deep);color:var(--footer-text);font-size:10px;line-height:48px;text-align:center}
</style>
</head>
<body>
<div class="page">
  <header class="site-header">
    <div class="brand">LOGO</div>
    <nav class="main-nav">
      <a href="#">Home</a>
      <a href="#" class="has-sub">States</a>
      <a href="#" class="has-sub">Programs</a>
      <a href="#" class="has-sub">Degrees</a>
      <a href="#">Accreditation</a>
      <a href="#">Rankings</a>
      <a href="#">Resources</a>
    </nav>
  </header>

  <section class="intro">
    <h1 class="definition">ac·cred·it·ed [uh-kred-i-tid] adj.</h1>
    <div class="video">
      <div class="video-still" role="img" aria-label="Video still: portraits of classical thinkers on a dark board"></div>
      <div class="video-title">Classical Education</div>
      <svg class="video-play" width="36" height="42" viewBox="0 0 36 42"><polygon points="0,0 36,21 0,42" fill="#ffffff"/></svg>
      <div class="video-controls">
        <svg style="left:8px" width="8" height="9" viewBox="0 0 8 9"><rect x="0" y="0" width="3" height="9" fill="#ccc"/><rect x="5" y="0" width="3" height="9" fill="#ccc"/></svg>
        <svg style="left:26px" width="10" height="9" viewBox="0 0 10 9"><polygon points="0,3 3,3 7,0 7,9 3,6 0,6" fill="#ccc"/></svg>
        <svg style="right:10px" width="9" height="9" viewBox="0 0 9 9"><rect x="0.5" y="0.5" width="8" height="8" fill="none" stroke="#ccc"/></svg>
      </div>
    </div>
    <p class="video-caption">Lorem ipsum dolor sit amet, consectetur adipisicing elit, sed<br>do eiusmod tempor incididunt ut labore et dolore magna aliqua.</p>

    <article class="overview">
      <h2>Overview</h2>
      <p>Lorem ipsum dolor sit amet, consectetur adipisicing elit, sed do eiusmod tempor incididunt ut labore et dolore magna aliqua. Ut enim ad minim veniam, quis nostrud exercitation ullamco laboris nisi ut aliquip ex ea commodo consequat.</p>
      <p>Lorem ipsum dolor sit amet, consectetur adipisicing elit, sed do eiusmod tempor incididunt ut labore et dolore magna aliqua. Ut enim ad minim veniam, quis nostrud exercitation ullamco laboris nisi ut aliquip ex ea commodo consequat. Lorem ipsum dolor sit amet, consectetur adipisicing elit, sed do eiusmod tempor incididunt ut labore et dolore magna aliqua.</p>
      <p>Lorem ipsum dolor sit amet, consectetur adipisicing elit, sed do eiusmod tempor incididunt ut labore et dolore magna aliqua. Ut enim ad minim veniam, quis nostrud exercitation ullamco laboris nisi ut aliquip ex ea commodo consequat. Lorem ipsum.</p>
    </article>
    <a href="#" class="read-more">Read More &gt;</a>
  </section>

  <section class="state-search">
    <div class="search-field">"Search Colleges by State"</div>
    <div class="search-button">
      <svg width="24" height="24" viewBox="0 0 24 24"><circle cx="10" cy="10" r="7" fill="none" stroke="#fff" stroke-width="2.5"/><line x1="15" y1="15" x2="22" y2="22" stroke="#fff" stroke-width="3" stroke-linecap="round"/></svg>
    </div>
  </section>

  <footer>
    <div class="site-footer">
      <ul class="footer-col col-about"><li>About Us</li><li>Terms and Condition</li><li>FAQ</li><li>Site Map</li></ul>
      <ul class="footer-col col-programs-a"><li>Accounting</li><li>Art</li><li>Bible</li><li>Business</li><li>Criminal Justice</li><li>Design</li><li>Education</li><li>Engineering</li><li>English</li></ul>
      <ul class="footer-col col-programs-b"><li>Law</li><li>LPN to RN</li><li>Management</li><li>Math</li><li>MBA</li><li>MPH</li><li>Medical Assisting</li><li>Military</li><li>Nursing</li></ul>
      <ul class="footer-col col-programs-c"><li>Occupational Therapy</li><li>Paralegal</li><li>Psychology</li><li>Pharmacy</li><li>RN to BSN</li><li>Social Work</li><li>Sonography</li></ul>
      <ul class="footer-col col-degrees"><li class="footer-heading">DEGREES</li><li>Certificate</li><li>Associate</li><li>Bachelors</li><li>Masters</li><li>PhD</li></ul>
    </div>
    <div class="copyright">Copyright © url.com. All Rights Reserved</div>
  </footer>
</div>
</body>
</html>
```